TITLE: What Makes My Child’s Playing Talent Grow? SUB-TITLE: A Mother’s Plain Talk Manual for Coaching...

My book is for parents who have young children that are really into sports. My book empowers parents so they can motivate their children to succeed. It deals with sports psychology. Both my title and subtitle should be easy to read. Ideally, I would like a picture of young athlete(s) on the title. I have uploaded files of some books on Brindlemart that deal with the same subject. The last two files are 1) my company logo, please try to include these colors 2) an ebook cover I put together myself. You will notice an On-line bonus in the middle of the book, this Bonus needs to be on the cover.

Target Market(s)

Parents with children who play sports at a high level

Colors

Designer to choose colors to be used in the design.

Requirements
Must have
• Online Bonus feature as per my example.
• Dimensions: Pagelux = The ideal size of your eBook cover art is a height/width ratio of 1.6:1. This means that for every 1,000 pixels in width, the image should be 1,600 pixels in height.
Nice to have
• picture of a young athlete or young athletes

```html
<!DOCTYPE html>
<html lang="en">
<head>
<meta charset="utf-8">
<title>What Makes My Child’s Playing Talent Grow? — Cover</title>
<link rel="stylesheet" href="https://fonts.googleapis.com/css2?family=Oswald:wght@300;400&family=Merriweather:wght@900&family=Montserrat:wght@400;500&display=swap">
<style>
  :root {
    --page-bg: #2b1a12;
    --tone-shadow: #2a1404;
    --tone-deep: #4a2606;
    --tone-mid: #8a4d10;
    --tone-warm: #b86c16;
    --tone-light: #dc9232;
    --tone-glow: #f0b45a;
    --type-cream: #fbf4e6;
    --type-shadow: rgba(30, 14, 2, 0.75);
    --seal-silver: #d9d9d9;
    --seal-edge: #9c9c9c;
    --seal-face: #f1f1f1;
    --seal-ink: #1d1d1d;
  }
  * { margin: 0; padding: 0; box-sizing: border-box; }
  html, body { width: 1200px; height: 1200px; overflow: hidden; }
  body { background: var(--page-bg); position: relative; }

  .cover {
    position: absolute;
    left: 260px;
    top: 56px;
    width: 680px;
    height: 1088px;
    overflow: hidden;
    box-shadow: 0 10px 40px rgba(0,0,0,0.55);
  }
  .cover-photo {
    position: absolute;
    inset: 0;
    background:
      radial-gradient(ellipse 26% 22% at 52% 40%, var(--tone-shadow) 0%, transparent 100%),
      radial-gradient(ellipse 30% 26% at 48% 60%, var(--tone-deep) 0%, transparent 100%),
      radial-gradient(ellipse 22% 40% at 92% 70%, var(--tone-deep) 0%, transparent 100%),
      radial-gradient(ellipse 34% 30% at 8% 30%, var(--tone-light) 0%, transparent 100%),
      radial-gradient(ellipse 40% 14% at 55% 88%, var(--tone-light) 0%, transparent 100%),
      radial-gradient(ellipse 20% 16% at 62% 50%, var(--tone-glow) 0%, transparent 100%),
      linear-gradient(180deg, var(--tone-warm) 0%, var(--tone-mid) 55%, var(--tone-warm) 85%, var(--tone-mid) 100%);
  }
  .title {
    position: absolute;
    left: 68px;
    top: 58px;
    width: 590px;
    font-family: "Oswald", sans-serif;
    font-weight: 400;
    font-size: 78px;
    line-height: 96px;
    text-transform: uppercase;
    color: var(--type-cream);
    text-shadow: 3px 3px 4px var(--type-shadow);
  }
  .subtitle {
    position: absolute;
    left: 68px;
    top: 350px;
    width: 580px;
    font-family: "Oswald", sans-serif;
    font-weight: 300;
    font-size: 30px;
    line-height: 35px;
    text-transform: uppercase;
    color: var(--type-cream);
    text-shadow: 2px 2px 3px var(--type-shadow);
  }
  .bonus-seal {
    position: absolute;
    left: 40px;
    top: 652px;
    width: 184px;
    height: 184px;
  }
  .bonus-text {
    position: absolute;
    left: 40px;
    top: 652px;
    width: 184px;
    height: 184px;
    display: flex;
    flex-direction: column;
    align-items: center;
    justify-content: center;
    color: var(--seal-ink);
    text-align: center;
  }
  .bonus-offer {
    font-family: "Merriweather", serif;
    font-weight: 900;
    font-size: 17px;
    line-height: 22px;
    text-transform: uppercase;
  }
  .bonus-value {
    font-family: "Montserrat", sans-serif;
    font-weight: 500;
    font-size: 22px;
    margin-top: 4px;
  }
  .bonus-note {
    font-family: "Montserrat", sans-serif;
    font-size: 9px;
  }
  .author {
    position: absolute;
    left: 0;
    width: 100%;
    top: 952px;
    padding-left: 140px;
    font-family: "Oswald", sans-serif;
    font-weight: 300;
    font-size: 68px;
    line-height: 80px;
    letter-spacing: 10px;
    text-transform: uppercase;
    white-space: nowrap;
    color: var(--type-cream);
    text-shadow: 3px 3px 4px var(--type-shadow);
  }
</style>
</head>
<body>
  <main class="cover">
    <div class="cover-photo" role="img" aria-label="Amber-toned photograph of a young basketball player in a dark jersey dribbling low past a defender on an indoor court, spectators blurred behind"></div>

    <h1 class="title">What Makes My<br>Child’s Playing<br>Talent Grow?</h1>
    <p class="subtitle">A Mother’s Plain Talk Manual for Coaching Confident, Focused and Resilient Athletes</p>

    <svg class="bonus-seal" viewBox="0 0 184 184" aria-hidden="true">
      <circle cx="92" cy="92" r="84" fill="var(--seal-silver)" stroke="var(--seal-edge)" stroke-width="14" stroke-dasharray="6 5"/>
      <circle cx="92" cy="92" r="78" fill="var(--seal-silver)"/>
      <circle cx="92" cy="92" r="72" fill="var(--seal-face)" stroke="var(--seal-edge)" stroke-width="2"/>
    </svg>
    <div class="bonus-text">
      <span class="bonus-offer">Free<br>Online<br>Workshop</span>
      <span class="bonus-value">$170 Value</span>
      <span class="bonus-note">Details Inside</span>
    </div>

    <p class="author">Leo Marvant</p>
  </main>
</body>
</html>
```